Law Firm Letterhead

We are looking for a letterhead for our military/veterans law firm. We like simplicity and clean, modern, flat, uncluttered designs. Our logo font is DIN 1451, and our website/business card info font is Helvetica Neue.

Required Information:

- Logo/Graphic: Please see attached logo / business card for ideas. Please also review firm website.

- Motto: A law firm for service members and veterans

- Web Address: www.brightharborcounsel.example

- Email: info@brightharborcounsel.example

- Phone: 866-214-3097

Colors: We prefer either a blue/grey or an all-blue color scheme. The blue in our logo is #336699.

Please DO NOT submit more than 3 designs. Spamming designs with only minor changes between the designs is not appreciated. We can evaluate your quality and direction by your best 1 or 2 designs.

Thank you!

```html
<!DOCTYPE html>
<html lang="en">
<head>
<meta charset="utf-8">
<title>Bright Harbor Counsel — Letterhead</title>
<link rel="stylesheet" href="https://fonts.googleapis.com/css2?family=Barlow+Condensed:wght@600&family=Arimo:wght@400;700&display=swap">
<style>
  :root {
    --brand-blue: #336699;
    --paper: #ffffff;
    --backdrop: #ecebe8;
    --contact-grey: #7a7a7a;
  }
  * { box-sizing: border-box; margin: 0; padding: 0; }
  html, body {
    width: 1200px;
    height: 1000px;
    overflow: hidden;
    background: var(--backdrop);
  }
  .letterhead {
    position: absolute;
    left: 265px;
    top: 61px;
    width: 670px;
    height: 867px;
    background: var(--paper);
    box-shadow: 0 4px 14px rgba(0, 0, 0, 0.18);
    overflow: hidden;
  }
  .masthead {
    position: absolute;
    left: 0;
    top: 0;
    width: 100%;
    height: 124px;
    background: var(--brand-blue);
  }
  .masthead-star {
    position: absolute;
    top: 46px;
    width: 32px;
    height: 32px;
  }
  .masthead-star--left { left: 45px; }
  .masthead-star--right { right: 48px; }
  .firm-name {
    position: absolute;
    left: 0;
    top: 42px;
    width: 100%;
    text-align: center;
    font-family: "Barlow Condensed", "Arial Narrow", sans-serif;
    font-weight: 600;
    font-size: 36px;
    letter-spacing: 0.5px;
    line-height: 40px;
    color: var(--paper);
  }
  .motto {
    position: absolute;
    left: 0;
    top: 148px;
    width: 100%;
    text-align: center;
    font-family: "Barlow Condensed", "Arial Narrow", sans-serif;
    font-weight: 600;
    font-size: 11px;
    letter-spacing: 0.2px;
    color: var(--brand-blue);
  }
  .motto-star {
    position: absolute;
    left: 327px;
    top: 171px;
    width: 16px;
    height: 16px;
  }
  .contact {
    position: absolute;
    right: 50px;
    top: 766px;
    text-align: right;
    font-family: Arimo, "Helvetica Neue", Arial, sans-serif;
    font-size: 12px;
    line-height: 20px;
    color: var(--contact-grey);
    list-style: none;
  }
  .contact-phone { font-weight: 700; }
</style>
</head>
<body>
  <main class="letterhead">
    <header class="masthead">
      <svg class="masthead-star masthead-star--left" viewBox="0 0 24 24" aria-hidden="true">
        <polygon fill="#ffffff" points="12,1 14.6,8.6 22.6,8.6 16.1,13.4 18.6,21.2 12,16.4 5.4,21.2 7.9,13.4 1.4,8.6 9.4,8.6"/>
      </svg>
      <h1 class="firm-name">BRIGHT HARBOR COUNSEL</h1>
      <svg class="masthead-star masthead-star--right" viewBox="0 0 24 24" aria-hidden="true">
        <polygon fill="#ffffff" points="12,1 14.6,8.6 22.6,8.6 16.1,13.4 18.6,21.2 12,16.4 5.4,21.2 7.9,13.4 1.4,8.6 9.4,8.6"/>
      </svg>
    </header>

    <p class="motto">A LAW FIRM FOR SERVICE MEMBERS AND VETERANS</p>
    <svg class="motto-star" viewBox="0 0 24 24" aria-hidden="true">
      <polygon fill="#336699" points="12,1 14.6,8.6 22.6,8.6 16.1,13.4 18.6,21.2 12,16.4 5.4,21.2 7.9,13.4 1.4,8.6 9.4,8.6"/>
    </svg>

    <ul class="contact">
      <li class="contact-phone">866-214-3097</li>
      <li class="contact-web">www.brightharborcounsel.example</li>
      <li class="contact-email">info@brightharborcounsel.example</li>
    </ul>
  </main>
</body>
</html>
```